Business Card Design

Looking for a professional looking business card for a carpentry/construction business that deals with renovations, extensions, homes, and anything carpentry based in Northern Australia. Would like to incorporate the attached logo with backgrounds of white, grey or maybe a close up of timber/wood grain. Thanks

Industry/Entity Type

Carpentry

Contact Information for Business Card

Dean Carlow, Owner, Po Box 2674 Katherine NT 0851, dean-carlow@fernmail.example, 0419563072, Builders Number: 293417CR

Requirements
Should not have
• Power tools/hand tools related to carpentry

```html
<!DOCTYPE html>
<html lang="en">
<head>
<meta charset="utf-8">
<title>Carlow Carpentry Business Card</title>
<link rel="stylesheet" href="https://fonts.googleapis.com/css2?family=Jost:wght@400;500;600&display=swap">
<style>
  :root {
    --sheet: #ffffff;
    --slate: #363435;
    --slate-edge: #2a2829;
    --leaf: #78a843;
    --ink-light: #ffffff;
    --wood-dark: #3b2014;
    --wood-mid: #6a3c22;
    --wood-warm: #86502d;
    --band: rgba(70, 60, 55, 0.72);
  }
  * { box-sizing: border-box; margin: 0; padding: 0; }
  html, body {
    width: 916px;
    height: 1200px;
    overflow: hidden;
    background: var(--sheet);
  }
  body {
    position: relative;
    font-family: "Jost", "Century Gothic", sans-serif;
  }
  .card {
    position: absolute;
    left: 0;
    width: 916px;
    overflow: hidden;
  }
  .card--front {
    top: 0;
    height: 590px;
    background: var(--slate);
    border: 1px solid var(--slate-edge);
  }
  .card--back {
    top: 610px;
    height: 590px;
  }
  .wood-grain {
    position: absolute;
    inset: 0;
    background:
      linear-gradient(90deg, var(--wood-dark) 0%, var(--wood-warm) 35%, var(--wood-mid) 55%, var(--wood-warm) 75%, var(--wood-dark) 100%);
  }
  .band {
    position: absolute;
    top: 305px;
    height: 221px;
    background: var(--band);
  }
  .band--brand { left: 0; width: 441px; }
  .band--details { left: 465px; width: 451px; }

  .brand {
    position: absolute;
    font-weight: 500;
    line-height: 1;
    display: flex;
    align-items: center;
    gap: 14px;
  }
  .brand__mark {
    width: 22px;
    height: 22px;
    background: currentColor;
    flex: none;
  }
  .brand__words { display: flex; flex-direction: column; }
  .brand__name { font-size: 78px; letter-spacing: -1px; }
  .brand__trade { font-size: 19px; letter-spacing: 1px; text-transform: uppercase; margin-top: 2px; align-self: flex-end; }

  .card--front .brand { left: 436px; top: 284px; color: var(--leaf); }
  .card--back .brand { left: 62px; top: 355px; color: var(--ink-light); }

  .contact {
    position: absolute;
    color: var(--ink-light);
    font-weight: 400;
  }
  .contact__name {
    font-size: 28px;
    line-height: 1;
    text-transform: uppercase;
    margin-bottom: 10px;
  }
  .contact__line {
    font-size: 22px;
    line-height: 27.5px;
  }
  .card--front .contact { left: 504px; top: 410px; }
  .card--back .contact { left: 495px; top: 354px; }
</style>
</head>
<body>
  <section class="card card--front">
    <div class="brand">
      <span class="brand__mark"></span>
      <div class="brand__words">
        <span class="brand__name">Carlow</span>
        <span class="brand__trade">Carpentry</span>
      </div>
    </div>
    <div class="contact">
      <p class="contact__name">Dean Carlow</p>
      <p class="contact__line">Po Box 2674, Katherine NT 0851</p>
      <p class="contact__line">Email : dean-carlow@fernmail.example</p>
      <p class="contact__line">Ph.: 0419563072,</p>
      <p class="contact__line">Builders Number: 293417CR</p>
    </div>
  </section>

  <section class="card card--back">
    <div class="wood-grain" role="img" aria-label="Close-up of vertical dark timber boards with wood grain"></div>
    <div class="band band--brand"></div>
    <div class="band band--details"></div>
    <div class="brand">
      <span class="brand__mark"></span>
      <div class="brand__words">
        <span class="brand__name">Carlow</span>
        <span class="brand__trade">Carpentry</span>
      </div>
    </div>
    <div class="contact">
      <p class="contact__name">Dean Carlow</p>
      <p class="contact__line">Po Box 2674, Katherine NT 0851</p>
      <p class="contact__line">Email : dean-carlow@fernmail.example</p>
      <p class="contact__line">Ph.: 0419563072,</p>
      <p class="contact__line">Builders Number: 293417CR</p>
    </div>
  </section>
</body>
</html>
```